Range of Mayonise Bottles

We are wanting a Logo and Artwork for a Range of Mayonnaise’s.
There are 3 lines in total
Mayonnaise Regular
Mayonnaise and Garlic
Aioli ( Mayo and Lemon)
All 300g Upside down Style Bottle.
Image attached.
Logo: is Brindle Pantry

Target Market(s)

Supermarket Line

Requirements
Must have
• Brindle Pantry must be on all 3 lines
Pictures on Front
weight on Front
Ingredinets Only English
we will provide Nutrtioanl Info so please leave space
Barcodes I will upload
Nice to have
• Image of Mayonaise

```html
<!DOCTYPE html>
<html lang="en">
<head>
<meta charset="utf-8">
<title>Brindle Pantry Mayonnaise Range – Labels</title>
<link href="https://fonts.googleapis.com/css2?family=Oswald:wght@500;600&family=Roboto+Condensed:wght@500;700&display=swap" rel="stylesheet">
<style>
  :root {
    --canvas: #ffffff;
    --navy-top: #1c55a8;
    --navy-bottom: #0b1a45;
    --brand-red: #d0262c;
    --white: #ffffff;
    --rule: #111111;
    --regular-band: #efb62a;
    --regular-weight: #6a2c14;
    --garlic-band: #bf8f98;
    --garlic-weight: #4a2238;
    --garlic-name: #e6b89c;
    --aioli-band: #2fb24a;
    --aioli-weight: #ffffff;
    --aioli-name: #3ec04f;
    --photo-top: #d8c3a3;
    --photo-bottom: #ece4d0;
  }
  * { box-sizing: border-box; margin: 0; padding: 0; }
  html, body { width: 1200px; height: 752px; overflow: hidden; background: var(--canvas); }
  .range {
    width: 1200px; height: 752px;
    display: flex; justify-content: center; align-items: center; gap: 70px;
  }
  .label {
    position: relative;
    width: 320px; height: 480px;
    border-radius: 150px 150px 170px 170px / 80px 80px 140px 140px;
    overflow: hidden;
    background: linear-gradient(180deg, var(--navy-top) 0%, var(--navy-bottom) 62%);
  }
  .brand {
    position: absolute; top: 0; left: 50%;
    transform: translateX(-50%);
    width: 190px; height: 92px;
    background: var(--brand-red);
    display: flex; justify-content: center; align-items: center;
  }
  .brand-name {
    color: var(--white);
    font-family: "Oswald", sans-serif; font-weight: 500;
    font-size: 26px; line-height: 1.05; text-align: center;
  }
  .product {
    position: absolute; top: 112px; width: 100%;
    text-align: center; color: var(--white);
    font-family: "Oswald", sans-serif; font-weight: 600;
    font-size: 50px; letter-spacing: 0.5px; line-height: 1;
  }
  .variant {
    position: absolute; top: 178px; width: 100%;
    text-align: center;
    font-family: "Roboto Condensed", sans-serif; font-weight: 500;
    font-size: 30px; letter-spacing: 4px; line-height: 1;
  }
  .variant--regular { color: var(--white); }
  .variant--garlic { color: var(--garlic-name); }
  .variant--aioli { color: var(--aioli-name); }
  .lower {
    position: absolute; left: 0; right: 0; top: 300px; bottom: 0;
    border-top: 3px solid var(--rule);
  }
  .serving-photo {
    position: absolute; inset: 0;
    background: linear-gradient(180deg, var(--photo-top) 0%, var(--photo-bottom) 100%);
  }
  .weight {
    position: absolute; left: 0; top: 0;
    width: 150px; height: 64px;
    display: flex; align-items: center; justify-content: center;
    font-family: "Roboto Condensed", sans-serif; font-weight: 700;
    font-size: 30px; line-height: 1;
  }
  .weight--regular { background: var(--regular-band); color: var(--regular-weight); }
  .weight--garlic { background: var(--garlic-band); color: var(--garlic-weight); }
  .weight--aioli { background: var(--aioli-band); color: var(--aioli-weight); }
</style>
</head>
<body>
  <main class="range">
    <article class="label">
      <div class="brand"><span class="brand-name">Brindle<br>Pantry</span></div>
      <h1 class="product">MAYONNAISE</h1>
      <p class="variant variant--regular">Regular</p>
      <div class="lower">
        <div class="serving-photo" role="img" aria-label="Photo of a bowl of mayonnaise beside a toasted ham and cheese sandwich"></div>
        <div class="weight weight--regular">300g</div>
      </div>
    </article>

    <article class="label">
      <div class="brand"><span class="brand-name">Brindle<br>Pantry</span></div>
      <h1 class="product">MAYONNAISE</h1>
      <p class="variant variant--garlic">Garlic</p>
      <div class="lower">
        <div class="serving-photo" role="img" aria-label="Photo of a bowl of garlic mayonnaise with garlic cloves and a toasted ham and cheese sandwich"></div>
        <div class="weight weight--garlic">300g</div>
      </div>
    </article>

    <article class="label">
      <div class="brand"><span class="brand-name">Brindle<br>Pantry</span></div>
      <h1 class="product">MAYONNAISE</h1>
      <p class="variant variant--aioli">Aioli</p>
      <div class="lower">
        <div class="serving-photo" role="img" aria-label="Photo of a bowl of aioli with a cut lime and a toasted ham and cheese sandwich"></div>
        <div class="weight weight--aioli">300g</div>
      </div>
    </article>
  </main>
</body>
</html>
```